Guarenteed! - Homepage Website Design - Coding not required- Winner to complete further pages

Hi all,

We're looking at redesigning our current website with a few adjustments to other pages but the main adjustments will be on the homepage which is what this design request is for. Please note : any of these ideas can be changed if you have something particularly different / special in mind etc.

P.S Coding is not required, just a design.

- Our website -

Our website is simply a price comparison website that allows customers to find companies within their area at the best price. The products available are mostly related to the vehicle trade and all refer to vinyl. This includes the likes of vehicle window tint, vehicle colour change vehicle wrap, vehicle signage as well as other cosmetic vinyl modifications. We allow the customer to search for their product within their chosen area and receive a list of companies who supply their product within that area. From here they can compare prices and view further details on the company.

- What we're looking to do -

We're looking first of all to adjust how the website homepage is displayed, this includes adding images and adjusting the colours that are explained below:

First of all, we look to spread out each of the 12 products (which can be seen on the website as it stands) and add an image to each of the products (all being spaced out as shown in our sketch)

We've been told the website looks too busy so we're thinking if we adjust the colours to more simplier neutral colours as well as the main focus of the website being on the 12 images, that would be great.

- Logo + Banner -

Logo to remain top left although banner may be removed / adjusted to make simplier.

- Colours -

Adjustments - Colours shades
We want the website to still look exciting but simplify the colours. Needs to be kept up to date with the colours / textures etc (bright colours to highlight keypoints)
We're still looking to use either blue or orange or maybe both to highlight these keypoints but the main website to be light colours and maybe even black on white background. The entire homepage can be adjusted colour wise if you feel it fits into your theme including menu bars, banners etc. The key is to get this right with being not too overpowering with the colours but still look interesting and up to date.

- 1 - 4 steps banner - (text may change)

This sits just under the logo and explains to the user how easy the website is to use and the steps they need to take. This may change to a 1 - 5 steps but we're looking to have this designed once the overall colours / theme of the website is sorted.

- 12 images - 4 x 3

This is the main focus of the website and will be the main focus of what the customer sees first of all. This will be where they select their product and then underneath, enter their postcode and distance they would like to search within. As explained further up, we have some of the product images available so if you can where possible add these to the design and then duplicate the images on those we currently don't have available.

- 12 Images -Titles -

These titles will be in this order from left to right and etc

- Colour Change Wrap
- Printed Vehicle Wrap
- Window Tint
- Headlight Tint
- Vehicle Signage
- Shop Signage
- Roof Vinyl Wrap
- Bonnet Vinyl Wrap
- Carbon Fibre Vinyl
- Stickerbomb Vinyl
- Clear Protective Vinyl
- Wheel Refurb

Text to be quite large, centered and with the o to the left of the title. Short titles like 'Window Tint' should fit on one line in the middle of the box where as titles such as ' Stickerbomb Vinyl Wrap' should have the 'Stickerbomb Vinyl' on the first line with the 'Wrap' on the line below. The background of this text is up to experient, might be worth just a simple colour or it might be worth using a bright blue or orange to keep in with the theme of the logo etc.

These will also have the circle tick box to the left of the title (as on the current website) where the customer clicks to select the product they have available.
We were also thinking that if when the customer ticks the circle on their selected box, the box is highlighted in some way to show this.

- Search Block -

This will appear under the 12 images and allows the customer to input their postcode and distance for the search criteria. Colours on this can of course be adjusted to keep in theme with the website.

- Under the 12 Images -

- Block underneath the 12 images and search block -

To the left will be some key bullet points about the website - maybe 4 or 5 with a green tick to the left of this. Background colour will probably be best to be a light colour, possibly grey.

Then to the right of this will appear 4 images, 2 before and 2 after when applying these products. Images to be used aren't fully decided on and we would like this stage of the design left to the end when the rest of the theme etc have been decided on.

Attached images are as follows :
- How the website looks as it stands
- The fold line on the website (obviously important)
- Our rough sketch of how we'd like the website homepage to look.
- We have 7 of the images ready that are all attached in this one file. Please duplicate the images on those that currently don't have the image available.

We will also be requesting a website developer to put this into action if our current designer falls through so please feel free to contact us if potentially interested.

The layout can change if you can think of something particular different / unique that works with this design. The main idea is to not only get the 12 products on view to the viewers but also the keypoints and before and after images.

Any questions, please ask away as we're bound to have forgotten a few things.

Thanks and good luck!

Hi all, keep the designs coming.

We haven't quite seen that extra special design we're after. As stated, we're after something fairly simple to suit the youth as well as the middle aged but we're also after something that bit special.

Colours to concentrate on are still and orange etc although feel free to use other colours if you have anything special in mind.

Please experience and we'll give you our honest feedback.

Many thanks all and good luck!

Hi all, this is a message to all the designers.

Some good designs coming in but we're still after that something special for the website design. Keep the designs coming and please feel free to experiment with the design colours, layout etc.

The basic principle of the website needs to remain regarding the 12 products, search within block and 4 steps all appearing on the homepage.

The 4 steps seems to work best when it's got text as well as some simple images next to this.

A variation with the product titles with how to display this, some designers have gone with a simple white background whereas others have gone with colours. Please experiment here and where possible, add a contract / texture to the colour. Please remember the product titles needs to be clear, centured and with the circle tick box to the left of it. 

We're after a fairly simple design although we need it to look 21st century, up to date as well as interesting. The key points straight away are the 4 steps as well as the 12 products so try to guide the viewer to these areas a little.

White background behind the 12 images seems to be a much, although a light colour could possibly work.

The keypoints underneath these 12 products are too very important as it outlines what we do etc. Tick colour can vary.

Next to these keypoints will be the 'before' and 'after' images, these images needs to be fairly small and ensure there is white background around the image itself.

Good luck all and any questions, feel free to ask away.

Thanks!

Hi,

 Thank you for your time and effort with these designs, we are very nearly there with the design but we've thought of something that may work for the homepage. A curved arrow from step 1 pointing to the products, this may or may not work but feel free to give it a go.

Many thanks,

Thank you to everyone for your time and efforts with the design. It's hugely appreciated so thank you all once again.

Wish you all the luck in the future.

```html
<!DOCTYPE html>
<html lang="en">
<head>
<meta charset="utf-8">
<title>WrapLocate – Homepage</title>
<link rel="stylesheet" href="https://fonts.googleapis.com/css2?family=Oswald:wght@300;400;600&family=Open+Sans:wght@400;600&display=swap">
<style>
  :root{
    --navy:#34406b;
    --orange:#eb9636;
    --orange-dark:#d9781b;
    --charcoal:#333638;
    --nav:#2f3133;
    --grey-band:#e6e7e8;
    --card-line:#d3d5d8;
    --white:#ffffff;
    --text-dark:#3a3f55;
    --muted:#a9abad;
  }
  *{box-sizing:border-box;margin:0;padding:0}
  html,body{width:851px;height:1200px;overflow:hidden;background:var(--white)}
  body{position:relative;font-family:"Open Sans",sans-serif}
  .abs{position:absolute}

  /* header */
  .brand{left:74px;top:20px;display:flex;align-items:center;gap:10px}
  .brand-dot{width:34px;height:34px;border-radius:50%;background:var(--orange)}
  .brand-name{font-family:"Oswald",sans-serif;font-weight:600;font-size:30px;color:var(--navy);letter-spacing:1px}
  .brand-tag{left:74px;top:62px;width:228px;height:12px;background:var(--navy);color:var(--white);font-size:8px;font-weight:600;text-align:center;line-height:12px;letter-spacing:.5px}

  .promo{left:370px;top:0;width:407px;height:88px;background:var(--orange);overflow:hidden}
  .promo-line{position:absolute;left:46px;background:var(--charcoal);color:var(--white);font-family:"Oswald",sans-serif;font-weight:600;font-size:17px;padding:0 4px;line-height:21px;letter-spacing:.5px}
  .promo-line.l1{top:12px}
  .promo-line.l2{top:34px}
  .promo-sub{position:absolute;left:46px;top:60px;font-family:"Oswald",sans-serif;font-weight:600;font-size:16px;color:var(--white);font-style:italic}
  .promo-map{position:absolute;left:280px;top:0;width:127px;height:88px;background:linear-gradient(135deg,#8aa34a,#c7a25a 60%,#e4d6b3)}

  /* nav */
  .nav{left:0;top:88px;width:851px;height:37px;background:var(--nav)}
  .nav ul{position:absolute;left:74px;top:0;list-style:none;display:flex;gap:23px;line-height:37px}
  .nav li{font-size:10.5px;font-weight:600;color:var(--white)}
  .nav li.active{color:var(--orange)}
  .search{position:absolute;left:582px;top:7px;width:195px;height:20px;background:#eeeeee;display:flex;align-items:center}
  .search span{font-size:9.5px;color:#999;font-style:italic;padding-left:6px;flex:1}
  .search .btn{width:20px;height:20px;background:#d9d9d9;display:flex;align-items:center;justify-content:center}

  /* steps */
  .steps{left:0;top:125px;width:851px;height:201px;background:var(--orange)}
  .step{position:absolute;top:32px;width:146px;height:146px;border-radius:50%;background:var(--charcoal);text-align:center;color:var(--white)}
  .step-num{position:absolute;left:0;top:-4px;width:38px;height:38px;border-radius:50%;background:var(--white);border:3px solid var(--navy);color:var(--navy);font-family:"Oswald",sans-serif;font-weight:600;font-size:20px;line-height:32px}
  .step-title{margin-top:40px;font-family:"Oswald",sans-serif;font-weight:400;font-size:17px;line-height:23px}
  .step-icon{margin-top:6px}

  /* products */
  .card{position:absolute;width:163px;height:155px;border:1px solid var(--card-line);background:var(--white)}
  .card-head{position:absolute;left:-1px;top:-1px;width:165px;height:48px}
  .card-title{position:absolute;left:0;top:6px;width:163px;text-align:center;font-family:"Oswald",sans-serif;font-weight:300;font-size:16px;color:var(--white)}
  .card-img{position:absolute;left:28px;top:62px;width:107px;height:76px;border-radius:6px}

  /* keypoints band */
  .band{left:0;top:886px;width:851px;height:200px;background:var(--grey-band)}
  .keys{left:74px;top:918px;list-style:none}
  .keys li{font-family:"Oswald",sans-serif;font-weight:300;font-size:15px;color:var(--text-dark);height:36px}
  .keys li::before{content:"›";margin-right:6px;font-weight:400}
  .gallery{left:318px;top:911px;width:459px;height:158px;background:var(--white);border-radius:6px}
  .g-label{position:absolute;top:6px;font-family:"Oswald",sans-serif;font-weight:300;font-size:15px;color:var(--navy)}
  .g-img{position:absolute;top:29px;width:194px;height:104px}
  .g-arrow{position:absolute;top:62px;font-size:30px;color:var(--charcoal);font-family:"Oswald",sans-serif}

  /* footer */
  .footer{left:0;top:1086px;width:851px;height:114px;background:var(--charcoal)}
  .f-links{position:absolute;left:74px;top:20px;list-style:none;display:flex;gap:23px}
  .f-links li{font-size:10.5px;font-weight:600;color:var(--muted)}
  .f-copy{position:absolute;left:74px;top:46px;font-size:9.5px;color:var(--muted)}
  .f-news{position:absolute;left:562px;top:25px;font-size:9.5px;font-weight:600;color:var(--muted)}
  .f-form{position:absolute;left:562px;top:43px;display:flex;height:21px}
  .f-form .in{width:152px;background:#1e1f20;border:1px solid #555;color:#777;font-size:9.5px;font-style:italic;padding-left:4px;line-height:19px}
  .f-form .sub{width:63px;background:#222;color:var(--white);font-size:9.5px;font-weight:600;text-align:center;line-height:21px}
  .social{position:absolute;top:78px;width:21px;height:21px;border-radius:2px}
</style>
</head>
<body>

<header>
  <div class="abs brand"><span class="brand-dot"></span><span class="brand-name">WrapLocate</span></div>
  <div class="abs brand-tag">Compare Local Vinyl Fitters</div>
  <div class="abs promo">
    <div class="promo-line l1">FIND A PROFESSIONAL</div>
    <div class="promo-line l2">VINYL INSTALLER TODAY</div>
    <div class="promo-sub">Search &amp; Save in Seconds!</div>
    <div class="promo-map" role="img" aria-label="Map of UK cities under a magnifying glass"></div>
  </div>
</header>

<nav class="abs nav">
  <ul>
    <li class="active">HOME</li><li>ABOUT US</li><li>CONTACT US</li><li>BLOG</li><li>LIST YOUR</li><li>COMPANY HERE</li>
  </ul>
  <div class="search"><span>Search</span>
    <div class="btn"><svg width="13" height="13" viewBox="0 0 13 13"><circle cx="5" cy="5" r="3.8" fill="none" stroke="#333" stroke-width="2"/><line x1="8" y1="8" x2="12" y2="12" stroke="#333" stroke-width="2.4"/></svg></div>
  </div>
</nav>

<section class="abs steps">
  <div class="step" style="left:77px">
    <div class="step-num">1</div>
    <div class="step-title">Select<br>Choosen Product</div>
    <svg class="step-icon" width="74" height="28" viewBox="0 0 74 28"><path d="M4 20 Q4 12 14 11 L22 4 Q34 0 48 4 L58 11 Q70 12 70 20 Z" fill="#fff"/><circle cx="19" cy="21" r="6" fill="#fff" stroke="#333638" stroke-width="2.5"/><circle cx="56" cy="21" r="6" fill="#fff" stroke="#333638" stroke-width="2.5"/></svg>
  </div>
  <div class="step" style="left:261px">
    <div class="step-num">2</div>
    <div class="step-title">Input Postcode<br>Distance + Search</div>
    <svg class="step-icon" width="40" height="40" viewBox="0 0 40 40"><circle cx="15" cy="15" r="11" fill="none" stroke="#fff" stroke-width="5"/><line x1="23" y1="23" x2="36" y2="36" stroke="#fff" stroke-width="7" stroke-linecap="round"/></svg>
  </div>
  <div class="step" style="left:445px">
    <div class="step-num">3</div>
    <div class="step-title">Compare<br>Companies + Prices</div>
    <svg class="step-icon" width="40" height="40" viewBox="0 0 40 40"><path d="M22 6 L34 6 L34 18 L16 36 L4 24 Z" fill="#fff"/><circle cx="28" cy="12" r="3" fill="#333638"/></svg>
  </div>
  <div class="step" style="left:630px">
    <div class="step-num">4</div>
    <div class="step-title">Contact<br>Choosen Company</div>
    <svg class="step-icon" width="40" height="40" viewBox="0 0 40 40"><circle cx="20" cy="20" r="17" fill="none" stroke="#fff" stroke-width="3"/><path d="M14 11 Q11 20 17 28 Q21 31 25 30 L24 25 L21 25 Q17 20 19 15 L21 14 L19 10 Z" fill="#fff"/></svg>
  </div>
</section>

<main>
  <svg width="0" height="0" style="position:absolute">
    <defs><path id="head" d="M6 0 H159 Q165 0 165 6 V40 Q82 56 0 40 V6 Q0 0 6 0 Z"/></defs>
  </svg>

  <!-- row 1 -->
  <div class="card" style="left:74px;top:358px"><svg class="card-head" viewBox="0 0 165 48"><use href="#head" fill="var(--navy)"/></svg><div class="card-title">Colour Change Wrap</div><div class="card-img" role="img" aria-label="White van" style="background:linear-gradient(#f1f2f3,#c9cbce)"></div></div>
  <div class="card" style="left:254px;top:358px"><svg class="card-head" viewBox="0 0 165 48"><use href="#head" fill="var(--navy)"/></svg><div class="card-title">Printed Vehicle Wrap</div><div class="card-img" role="img" aria-label="Van with printed green and sky wrap" style="background:linear-gradient(#9ec2e2,#e9efe6 50%,#3f8a2f)"></div></div>
  <div class="card" style="left:434px;top:358px"><svg class="card-head" viewBox="0 0 165 48"><use href="#head" fill="var(--navy)"/></svg><div class="card-title">Window Tint</div><div class="card-img" role="img" aria-label="Two green hatchbacks with tinted windows" style="background:linear-gradient(#fff 20%,#52b848 50%,#fff 85%)"></div></div>
  <div class="card" style="left:614px;top:358px"><svg class="card-head" viewBox="0 0 165 48"><use href="#head" fill="var(--navy)"/></svg><div class="card-title">Headlight Tint</div><div class="card-img" role="img" aria-label="Dark sports car front with tinted headlights" style="background:linear-gradient(#fff,#3b3d40 45%,#7b7d80 80%,#fff)"></div></div>

  <!-- row 2 -->
  <div class="card" style="left:74px;top:534px"><svg class="card-head" viewBox="0 0 165 48"><use href="#head" fill="var(--navy)"/></svg><div class="card-title">Vehicle Signage</div><div class="card-img" role="img" aria-label="Van with green and black signage" style="background:linear-gradient(90deg,#2f3133,#a7c23b 50%,#f2f2f2)"></div></div>
  <div class="card" style="left:254px;top:534px"><svg class="card-head" viewBox="0 0 165 48"><use href="#head" fill="var(--navy)"/></svg><div class="card-title">Shop Signage</div><div class="card-img" role="img" aria-label="Shop front with sign above windows" style="background:linear-gradient(#e3e6ea,#3a3d42 40%,#d7dbe0)"></div></div>
  <div class="card" style="left:434px;top:534px"><svg class="card-head" viewBox="0 0 165 48"><use href="#head" fill="var(--navy)"/></svg><div class="card-title">Roof Vinyl Wrap</div><div class="card-img" role="img" aria-label="Silver car with black roof wrap" style="background:radial-gradient(#5a5c60,#b8babd 55%,#fff 80%)"></div></div>
  <div class="card" style="left:614px;top:534px"><svg class="card-head" viewBox="0 0 165 48"><use href="#head" fill="var(--navy)"/></svg><div class="card-title">Bonnet Winyl Wrap</div><div class="card-img" role="img" aria-label="Silver car with black bonnet wrap" style="background:radial-gradient(#5a5c60,#b8babd 55%,#fff 80%)"></div></div>

  <!-- row 3 -->
  <div class="card" style="left:74px;top:712px"><svg class="card-head" viewBox="0 0 165 48"><use href="#head" fill="var(--navy)"/></svg><div class="card-title">Carbon Fibre Vinyl</div><div class="card-img" role="img" aria-label="Silver hatchback with carbon fibre details" style="background:radial-gradient(#8e9094,#c8cacd 55%,#fff 80%)"></div></div>
  <div class="card" style="left:254px;top:712px"><svg class="card-head" viewBox="0 0 165 48"><use href="#head" fill="var(--navy)"/></svg><div class="card-title">StickerBomb Vinyl</div><div class="card-img" role="img" aria-label="Car bonnet covered in colourful stickers" style="background:linear-gradient(135deg,#e5e5e5,#e8b83c 35%,#4aa3d8 55%,#d94a3a 70%,#e5e5e5)"></div></div>
  <div class="card" style="left:434px;top:712px"><svg class="card-head" viewBox="0 0 165 48"><use href="#head" fill="var(--navy)"/></svg><div class="card-title">Clear Protective Vinyl</div><div class="card-img" role="img" aria-label="Roll of clear protective film" style="background:linear-gradient(160deg,#fff 30%,#e4e6e8 50%,#f5e27a 70%,#fff)"></div></div>
  <div class="card" style="left:614px;top:712px"><svg class="card-head" viewBox="0 0 165 48"><use href="#head" fill="var(--navy)"/></svg><div class="card-title">Wheel Refurb</div><div class="card-img" role="img" aria-label="Group of alloy wheels" style="background:radial-gradient(#f2f2f2,#8f9296 50%,#fff 80%)"></div></div>
</main>

<section class="abs band"></section>
<ul class="abs keys">
  <li>Compare Products, Location and Prices</li>
  <li>Installers throughout the Country</li>
  <li>Available throughout the Country</li>
  <li>Quick, Easy and Free to Search</li>
</ul>
<div class="abs gallery">
  <div class="g-label" style="left:101px">Before</div>
  <div class="g-label" style="left:286px">After</div>
  <div class="g-arrow" style="left:20px">‹</div>
  <div class="g-img" style="left:36px" role="img" aria-label="White pickup truck before wrapping" aria-hidden="false"><div style="width:100%;height:100%;background:linear-gradient(#f3f4f6,#d7d9dc 55%,#eef0f2)"></div></div>
  <div class="g-img" style="left:230px" role="img" aria-label="Pickup truck after colourful wrap"><div style="width:100%;height:100%;background:linear-gradient(#f3f4f6,#3f9fc4 45%,#7fbf4a 65%,#eef0f2)"></div></div>
  <div class="g-arrow" style="left:436px">›</div>
</div>

<footer class="abs footer">
  <ul class="f-links"><li>ABOUT US</li><li>CONTACT US</li><li>BLOG</li><li>LIST YOUR COMPANY HERE</li></ul>
  <div class="f-copy">All Rights Reserved. Copyrights @ 2013</div>
  <div class="f-news">Newsletter</div>
  <div class="f-form"><div class="in">Enter your Mail ID</div><div class="sub">SUBSCRIBE</div></div>
  <span class="social" style="left:633px;background:#3b5a9a"></span>
  <span class="social" style="left:662px;background:#3aa6e0"></span>
  <span class="social" style="left:693px;background:#2a7ab8"></span>
  <span class="social" style="left:725px;background:#f08a1e"></span>
  <span class="social" style="left:756px;background:#d6402e"></span>
</footer>

</body>
</html>
```